Lodging Venture Advisors

I am an independent operator engaged on short/medium term consultancy briefs within the Hotel/Resort sector in the Pacific Area and have a representation in Fiji.

A broad based services is offered and includes:

Development Advisory
Property Management
Sales & Marketing
Holiday Ownership/Timeshare
Resorts/Apartments/Motels/Flashpackers/B&B
Financial & Legal Referrals

Industry/Entity Type

Hotel

Contact Information for Business Card

Business name - LODGING VENTURE ADVISORS
My name - Grant Whitlock
Address: PO Box 382 Coral Heights 4219 Qld
Phone: Australia: +61 7 55904283 Mobile: 0418952064 (Viber)
Fiji: +679 8527319
Email: grantmwhitlock@netmailbox.example

```html
<!DOCTYPE html>
<html lang="en">
<head>
<meta charset="utf-8">
<title>Lodging Venture Advisors – Business Card</title>
<link rel="stylesheet" href="https://fonts.googleapis.com/css2?family=Lato:wght@300;400;700;900&display=swap">
<style>
  :root {
    --page: #ffffff;
    --charcoal: #232324;
    --brand-blue: #0f74bc;
    --blue-edge: #4c6a86;
    --card-grey: #e6e7e9;
    --ink: #111111;
    --ink-soft: #3a3a3a;
    --white: #ffffff;
  }
  * { margin: 0; padding: 0; box-sizing: border-box; }
  html, body {
    width: 1200px; height: 900px; overflow: hidden;
    background: var(--page);
    font-family: "Lato", Arial, sans-serif;
  }
  .canvas { position: relative; width: 1200px; height: 900px; }

  /* Front of card */
  .card-front {
    position: absolute; left: 263px; top: 51px;
    width: 654px; height: 374px;
  }
  .card-front svg { display: block; }
  .front-bg { fill: var(--charcoal); }
  .front-band { fill: var(--brand-blue); }
  .front-title {
    fill: var(--white);
    font-family: "Lato", Arial, sans-serif;
    font-weight: 900;
    font-size: 33px;
    letter-spacing: 0.2px;
  }

  /* Back of card */
  .card-back {
    position: absolute; left: 261px; top: 478px;
    width: 657px; height: 376px;
    background: var(--card-grey);
    overflow: hidden;
  }
  .name-marker {
    position: absolute; left: 0; top: 47px;
    width: 44px; height: 46px; background: var(--brand-blue);
  }
  .name-rule {
    position: absolute; left: 57px; top: 45px;
    width: 8px; height: 50px; background: var(--charcoal);
  }
  .holder { position: absolute; left: 81px; top: 42px; }
  .holder-name {
    font-weight: 700; font-size: 26px; color: var(--ink);
    line-height: 1.1; letter-spacing: 0.2px;
  }
  .holder-role {
    font-weight: 300; font-size: 17px; color: var(--ink-soft);
    margin-top: 3px;
  }

  .contact-list { position: absolute; left: 26px; top: 175px; list-style: none; }
  .contact-item {
    display: flex; align-items: center;
    height: 34px;
    font-weight: 300; font-size: 19px; color: var(--ink-soft);
  }
  .contact-item:first-child { height: 22px; margin-bottom: 15px; }
  .contact-tag {
    width: 23px; height: 20px; margin-right: 10px;
    background: var(--brand-blue); color: var(--ink);
    font-weight: 400; font-size: 15px;
    display: flex; align-items: center; justify-content: center;
  }
  .contact-item:first-child .contact-tag { margin-right: 10px; }

  .side-panel {
    position: absolute; left: 545px; width: 83px;
    background: var(--brand-blue);
    border: 1px solid var(--blue-edge);
  }
  .side-panel.upper { top: -1px; height: 178px; }
  .side-panel.lower { top: 199px; height: 178px; }
  .monogram {
    position: absolute; left: 0; right: 0; top: 44px;
    text-align: center;
    font-weight: 400; font-size: 22px; color: var(--ink); letter-spacing: 0.5px;
  }
  .monogram-bar {
    position: absolute; left: 11px; top: 78px;
    width: 53px; height: 8px; background: var(--charcoal);
  }
</style>
</head>
<body>
<main class="canvas">
  <section class="card-front" aria-label="Card front">
    <svg width="654" height="374" viewBox="0 0 654 374">
      <rect class="front-bg" width="654" height="374"/>
      <polygon class="front-band" points="0,169 654,77 654,204 0,296"/>
      <text class="front-title" x="327" y="197" text-anchor="middle" transform="rotate(-8 327 187)">LODGING VENTURE ADVISORS</text>
    </svg>
  </section>

  <section class="card-back" aria-label="Card back">
    <div class="name-marker"></div>
    <div class="name-rule"></div>
    <div class="holder">
      <h1 class="holder-name">GRANT WHITLOCK</h1>
      <p class="holder-role">Development Advisory</p>
    </div>

    <ul class="contact-list">
      <li class="contact-item"><span class="contact-tag">A</span>PO Box 382 Coral Heights 4219 Qld</li>
      <li class="contact-item"><span class="contact-tag">P</span>+61 7 55904283</li>
      <li class="contact-item"><span class="contact-tag">M</span>0418952064</li>
      <li class="contact-item"><span class="contact-tag">V</span>+679 8527319</li>
      <li class="contact-item"><span class="contact-tag">E</span>grantmwhitlock@netmailbox.example</li>
    </ul>

    <div class="side-panel upper">
      <div class="monogram">LVA</div>
      <div class="monogram-bar"></div>
    </div>
    <div class="side-panel lower"></div>
  </section>
</main>
</body>
</html>
```